Austrian finance und insurance broker needs business card design

We Need a serious looking Design for Business Card. we consult private and corporates customers in finance and insurance questions. the final design should express security and experience. We consult customers in questions of loans, Investments and insurance and have a wide range of Banks to offer. We compare several offers and select the best for our customers.

Target Market(s)

private and coporate customers with efforts in Money and insurance

Industry/Entity Type

Insurance Broker

Contact Information for Business Card

Martin Brauneder
Geschäftsführer
staatl. geprüfter Vermögensberater und Versicherungsmakler
Tel: 0664 512 8049
office@der-brauneder.at
www.der-brauneder.at
Anton Weibl Gasse 14
2135 Halbach
GISA Nr. 40527318 u. 40816493 (backside)

Font styles to use
Serif
Sans Serif

Requirements
Must have
• logo (designcrowd zip) and all Details
Nice to have
• makler logo design, maybe a 2 coloured Version is possible

```html
<!DOCTYPE html>
<html lang="de">
<head>
<meta charset="utf-8">
<title>Brauneder Vermögensberatung – Visitenkarte</title>
<link rel="stylesheet" href="https://fonts.googleapis.com/css2?family=Lato:wght@400;700&family=Montserrat:wght@600;700&display=swap">
<style>
  :root {
    --backdrop: #2e2a28;
    --paper: #ffffff;
    --brand-blue: #1a55b8;
    --brand-grey: #5f5f5f;
    --text-dark: #2b2b2b;
    --rule: #444444;
    --badge-red: #b3202f;
  }
  html, body {
    margin: 0;
    width: 1200px;
    height: 844px;
    overflow: hidden;
    background: var(--backdrop);
  }
  .stage {
    position: relative;
    width: 1200px;
    height: 844px;
  }
  .card {
    position: absolute;
    top: 272px;
    width: 510px;
    height: 300px;
    box-shadow: 0 14px 30px rgba(0,0,0,.45);
    overflow: hidden;
  }
  .card-front { left: 60px; background: var(--paper); }
  .card-back  { left: 630px; background: var(--brand-grey); }

  /* front */
  .brand-lockup {
    position: absolute;
    top: 30px;
    left: 232px;
    display: flex;
    align-items: center;
    gap: 10px;
  }
  .brand-dot {
    width: 30px;
    height: 30px;
    border-radius: 50%;
    background: var(--brand-blue);
    flex: none;
  }
  .brand-name {
    font-family: "Montserrat", sans-serif;
    font-weight: 600;
    font-size: 14px;
    color: var(--brand-blue);
    line-height: 1.2;
  }
  .partner-badge {
    position: absolute;
    top: 98px;
    left: 40px;
    width: 54px;
    height: 54px;
    border-radius: 50%;
    background: var(--badge-red);
  }
  .rule {
    position: absolute;
    right: 36px;
    height: 1px;
    background: var(--rule);
  }
  .rule-top    { top: 86px;  left: 232px; }
  .rule-mid    { top: 228px; left: 40px; }
  .rule-bottom { top: 262px; left: 40px; }
  .person {
    position: absolute;
    top: 156px;
    left: 40px;
    font-family: "Lato", sans-serif;
    color: var(--text-dark);
    font-size: 14px;
    line-height: 1.3;
    white-space: nowrap;
  }
  .person-name {
    margin: 0 0 2px;
    font-family: "Montserrat", sans-serif;
    font-weight: 700;
    font-size: 19px;
    line-height: 1.2;
    color: var(--brand-blue);
  }
  .person-role { margin: 0; }
  .contact-line {
    position: absolute;
    top: 237px;
    left: 40px;
    font-family: "Lato", sans-serif;
    font-size: 12.5px;
    color: var(--text-dark);
    white-space: nowrap;
  }
  .contact-line .label, .contact-line .web { color: var(--brand-blue); }
  .address {
    position: absolute;
    top: 270px;
    left: 40px;
    font-family: "Lato", sans-serif;
    font-size: 14px;
    color: var(--text-dark);
    white-space: nowrap;
  }

  /* back */
  .back-art { position: absolute; inset: 0; }
  .back-name {
    position: absolute;
    top: 108px;
    left: 230px;
    width: 230px;
    text-align: center;
    font-family: "Montserrat", sans-serif;
    font-weight: 700;
    font-size: 30px;
    color: var(--paper);
  }
  .gisa {
    position: absolute;
    right: 30px;
    bottom: 28px;
    font-family: "Lato", sans-serif;
    font-size: 13px;
    color: var(--paper);
  }
</style>
</head>
<body>
<main class="stage">

  <section class="card card-front" aria-label="Visitenkarte Vorderseite">
    <div class="brand-lockup">
      <span class="brand-dot"></span>
      <span class="brand-name">Brauneder<br>Vermögensberatung GmbH</span>
    </div>
    <div class="rule rule-top"></div>
    <div class="partner-badge" role="img" aria-label="Versicherungsmakler-Abzeichen"></div>
    <div class="person">
      <h1 class="person-name">Martin Brauneder</h1>
      <p class="person-role">Geschäftsführer</p>
      <p class="person-role">staatl. geprüfter Vermögensberater und Versicherungsmakler</p>
    </div>
    <div class="rule rule-mid"></div>
    <div class="contact-line">
      <span class="label">P:</span> 0664 512 8049 | <span class="label">E:</span> office@der-brauneder.at | <span class="web">www.der-brauneder.at</span>
    </div>
    <div class="rule rule-bottom"></div>
    <div class="address">Anton Weibl Gasse 14 2135 Halbach</div>
  </section>

  <section class="card card-back" aria-label="Visitenkarte Rückseite">
    <svg class="back-art" width="510" height="300" viewBox="0 0 510 300" aria-hidden="true">
      <rect width="510" height="300" fill="var(--brand-grey)"/>
      <polygon points="0,0 250,0 200,300 0,300" fill="var(--brand-blue)"/>
      <rect x="160" y="210" width="280" height="90" fill="var(--brand-blue)"/>
      <circle cx="345" cy="125" r="150" fill="var(--brand-grey)"/>
    </svg>
    <div class="back-name">Brauneder</div>
    <div class="gisa">GISA Nr. 40527318 u. 40816493</div>
  </section>

</main>
</body>
</html>
```